Cousin Fenwick's Filmaro Project

Create a design with the words, "Cousin Fenwick's Fil-maro Kit". This design will be featured on the product itself. The product will entail a kit of items to help auto body and painters make repairs. The kit itself will be at least one foot long/wide when packaged.

The design should be more than just the logo....it will need to be on the cover of the product which is approx 8" by 8".

Target Market(s)

Anyone who repairs fiberglass, hard surface products for a living...auto, boats, decks, drywall, etc. Largely blue collar DIY men.

Requirements
Must have
• Some of the design must have a see-through/clear section so that customers can see what is in the package.
Nice to have
• In an ideal world, the design could be expanded or shrunk but should be about 1" high.
Should not have
• No cartoon characters.

```html
<!DOCTYPE html>
<html lang="en">
<head>
<meta charset="utf-8">
<title>Cousin Fenwick's Fil-maro Kit</title>
<link rel="stylesheet" href="https://fonts.googleapis.com/css2?family=Montserrat:ital,wght@0,400;0,500;0,800;1,800&family=Fira+Sans+Condensed:wght@400&display=swap">
<style>
  :root {
    --sky: #35c3f0;
    --ink: #231f20;
    --paper: #ffffff;
    --powder-light: #eef0f4;
    --powder-shade: #bfc3cc;
  }
  html, body {
    margin: 0;
    padding: 0;
    width: 1200px;
    height: 1000px;
    overflow: hidden;
    background: var(--paper);
  }
  .canvas {
    position: relative;
    width: 1200px;
    height: 1000px;
    font-family: "Montserrat", Arial, sans-serif;
  }
  .package-cover {
    position: absolute;
    left: 252px;
    top: 152px;
    width: 697px;
    height: 697px;
    background: var(--sky);
    overflow: hidden;
  }
  .cover-shapes {
    position: absolute;
    left: 0;
    top: 0;
  }
  .brand-name {
    position: absolute;
    right: 48px;
    top: 196px;
    margin: 0;
    font-weight: 800;
    font-size: 45px;
    letter-spacing: 0.5px;
    color: var(--ink);
    line-height: 1;
    white-space: nowrap;
  }
  .product-band {
    position: absolute;
    left: 0;
    top: 250px;
    width: 697px;
    height: 31px;
    background: var(--ink);
  }
  .product-name {
    position: absolute;
    left: 214px;
    top: 1px;
    margin: 0;
    font-weight: 800;
    font-style: italic;
    font-size: 24px;
    color: var(--paper);
    line-height: 30px;
  }
  .product-description {
    position: absolute;
    left: 214px;
    top: 298px;
    width: 470px;
    margin: 0;
    font-weight: 500;
    font-size: 9.6px;
    line-height: 11.5px;
    color: var(--ink);
  }
  .feature-pill {
    position: absolute;
    left: 345px;
    top: 345px;
    width: 352px;
    height: 25px;
    background: var(--ink);
    border-radius: 12.5px 0 0 12.5px;
    margin: 0;
    padding: 0;
    list-style: none;
    font-family: "Fira Sans Condensed", "Arial Narrow", sans-serif;
    font-size: 12.5px;
    color: var(--paper);
  }
  .feature-pill li {
    position: absolute;
    top: 0;
    line-height: 25px;
  }
  .feature-pill li::before {
    content: "\2022";
    margin-right: 4px;
  }
  .feature-paintable { left: 17px; }
  .feature-permanent { left: 118px; }
  .feature-nonshrinking { left: 229px; }
  .contents-window {
    position: absolute;
    left: 518px;
    top: 490px;
    width: 150px;
    height: 150px;
    border: 4px solid var(--ink);
    border-radius: 22px;
    background: radial-gradient(circle at 40% 35%, var(--powder-light), var(--powder-shade));
  }
  .net-weight {
    position: absolute;
    left: 15px;
    top: 656px;
    margin: 0;
    font-size: 14px;
    color: var(--paper);
    font-weight: 400;
  }
  .net-weight strong {
    font-weight: 500;
  }
</style>
</head>
<body>
<div class="canvas">
  <section class="package-cover">
    <svg class="cover-shapes" width="697" height="697" viewBox="0 0 697 697">
      <polygon class="corner-block-top" points="0,0 278,0 97,159 0,159" fill="var(--ink)"/>
      <polygon class="accent-stripe-top" points="278,0 320,0 170,132 128,132" fill="var(--paper)"/>
      <polygon class="corner-block-bottom" points="0,398 97,398 438,697 0,697" fill="var(--ink)"/>
      <polygon class="accent-stripe-bottom" points="126,425 253,425 566,697 438,697" fill="var(--paper)"/>

      <g class="use-badge" role="img" aria-label="Boat repair icon">
        <circle cx="245" cy="475" r="32" fill="var(--ink)"/>
        <circle cx="245" cy="475" r="37" fill="none" stroke="var(--sky)" stroke-width="4"
                stroke-dasharray="120 233" transform="rotate(-100 245 475)"/>
      </g>
      <g class="use-badge" role="img" aria-label="Wall and drywall repair icon">
        <circle cx="346" cy="565" r="32" fill="var(--ink)"/>
        <circle cx="346" cy="565" r="37" fill="none" stroke="var(--sky)" stroke-width="4"
                stroke-dasharray="120 233" transform="rotate(-100 346 565)"/>
      </g>
      <g class="use-badge" role="img" aria-label="Auto body repair icon">
        <circle cx="450" cy="654" r="32" fill="var(--ink)"/>
        <circle cx="450" cy="654" r="37" fill="none" stroke="var(--sky)" stroke-width="4"
                stroke-dasharray="120 233" transform="rotate(-100 450 654)"/>
      </g>
    </svg>

    <h1 class="brand-name">COUSIN FENWICK'S</h1>

    <div class="product-band">
      <h2 class="product-name">Fil-maro Kit</h2>
    </div>

    <p class="product-description">Lorem ipsum dolor sit amet, consectetuer adipiscing elit, sed diam nonummy nibh euismod tincidunt ut laoreet dolore magna aliquam erat volutpat. Ut wisi enim ad</p>

    <ul class="feature-pill">
      <li class="feature-paintable">Paintable</li>
      <li class="feature-permanent">Permanent</li>
      <li class="feature-nonshrinking">Non-Shrinking</li>
    </ul>

    <div class="contents-window" role="img" aria-label="Clear window showing the white filler powder inside"></div>

    <p class="net-weight"><strong>Net Wt.</strong> 7.56 lb</p>
  </section>
</div>
</body>
</html>
```